Website design for learning and development business

I need a logo for my new business based in Australasia. I am a kiwi who is a creative change maker working in the Learning & development space. I design experiential learning opportunities for businesses to grow and nurture their tribes. I take a holistic look at an organisation and analyse what is needed to build a positive culture with a growth mindset woven into their DNA. I would like to see designs that are based on the following word snaps - creative, interesting, tribal, journey, adaptability, engaging, fluid, architectural, bespoke, courageous, challenging .I have the logo (attached) and I Need a startup business website designed. I am a Learning and development professional who is looking at going out on my own and establishing my own business. I would like a website designed that people would go to to check out what I do, how I do, what skills I have and how to contact me. Also room for a blog/articles.

Target Market(s)

Small to medium business

Industry/Entity Type

Self employed training and consultancy company

Number of Pages Required

5+ page

Requirements
Must have
• home page, about page, contact us page, blog page, search for us page
Nice to have
• Testimonials,

```html
<!DOCTYPE html>
<html lang="en">
<head>
<meta charset="utf-8">
<title>Tideway — Learning &amp; Development</title>
<link href="https://fonts.googleapis.com/css2?family=Poppins:wght@300;400;500;600;700&display=swap" rel="stylesheet">
<style>
:root{
  --navy:#24427f;
  --navy-dark:#1d3670;
  --ink:#1f2a44;
  --text:#4a5160;
  --muted:#9aa1ad;
  --line:#e3e6ec;
  --soft:#f5f7fb;
  --footer:#15181f;
  --white:#fff;
}
*{box-sizing:border-box;margin:0;padding:0}
html,body{width:1200px;height:5025px;overflow:hidden}
body{font-family:'Poppins',sans-serif;color:var(--text);background:var(--white);position:relative}
.abs{position:absolute}
.section{position:absolute;left:0;width:1200px}
.heading{font-weight:300;color:var(--navy);font-size:30px;line-height:1.2;white-space:nowrap}
.heading b{font-weight:600}
.small{font-size:10px;line-height:19px;color:var(--muted)}
.btn{position:absolute;display:flex;align-items:center;justify-content:center;font-size:9px;font-weight:500;color:var(--ink);border:1px solid var(--line);border-radius:3px;background:#fff}
.photo{position:absolute}

.brand{font-weight:600;font-size:20px;color:var(--ink);display:flex;align-items:center;gap:7px}
.brand i{width:18px;height:18px;border-radius:50%;background:var(--navy);display:block}
.nav{top:92px;left:234px;width:730px;height:48px;background:var(--navy);display:flex;align-items:center;padding:0 30px;z-index:2}
.nav a{color:#fff;font-size:12px;text-decoration:none;margin-right:16px}
.nav a+a::before{content:"\2022";margin-right:12px;font-size:8px}
.search{position:absolute;right:0;top:0;height:48px;width:190px;background:var(--navy-dark);color:#7f93bd;font-size:10px;display:flex;align-items:center;padding-left:12px}

.hero-title{font-size:40px;font-weight:300;color:var(--navy);line-height:45px;white-space:nowrap}
.hero-title b{font-weight:600}

.feat h3{font-size:13px;font-weight:500;color:var(--ink);margin-bottom:12px}
.feat p{width:220px}
.hex{position:absolute;width:54px;height:58px}
.svc h3{font-size:13px;font-weight:500;color:var(--ink);margin-bottom:9px}
.svc p{width:155px;font-size:9.5px;line-height:18px;color:var(--muted)}

.stat{color:#fff}
.stat b{font-size:30px;font-weight:400;display:block;line-height:36px}
.stat span{font-size:10px;color:#c9d3e8}

.member .ph{width:168px;height:174px}
.member h4{font-size:12px;font-weight:600;color:var(--navy);margin-top:18px}
.member span{font-size:9px;color:var(--muted)}

.quote{background:#fff;box-shadow:0 6px 24px rgba(30,45,80,.08);padding:28px 30px 0 52px;font-size:11px;line-height:22px;color:var(--text)}
.quote::before{content:"\201C";position:absolute;left:22px;top:14px;font-size:44px;color:var(--navy);font-weight:700;line-height:1}

.field{position:absolute;border:1px solid rgba(255,255,255,.25);color:#cfd8ec;font-size:10px;padding:10px 14px}

.card{position:absolute;border:1px solid var(--line);background:#fff}
.card .ph{height:157px}
.card .body{padding:14px 20px}
.card em{font-style:normal;font-size:9px;color:var(--muted)}
.card h4{font-size:12px;font-weight:600;color:var(--navy);margin:4px 0 6px}
.card p{font-size:9.5px;line-height:17px;color:var(--muted)}
.card a{font-size:9.5px;color:var(--ink);font-weight:500;text-decoration:none;display:block;margin-top:10px}

.partner{position:absolute;height:76px;border:1px solid var(--line);display:flex;align-items:center;justify-content:center}
.partner i{width:78px;height:22px;border-radius:11px;background:#e6e9ef;display:block}

.footer{top:4640px;height:385px;background:var(--footer);color:#b4b9c4}
.footer h5{color:#fff;font-size:14px;font-weight:500;margin-bottom:22px}
.footer li{list-style:none;font-size:10px;line-height:24px}
.footer li::before{content:"\203A";margin-right:8px}
.social{display:flex;gap:10px}
.social i{width:22px;height:22px;border-radius:50%;border:1px solid #4d5361;display:block}
</style>
</head>
<body>

<header class="section" style="top:0;height:92px">
  <div class="brand abs" style="left:234px;top:31px"><i></i>Tideway</div>
  <div class="abs" style="left:630px;top:26px;width:36px;height:36px;border-radius:50%;border:1px solid var(--line)">
    <svg width="36" height="36" viewBox="0 0 36 36"><path d="M13 11l4 0 1 4-2 2q2 4 5 5l2-2 4 1 0 4q-11 1-14-14z" fill="none" stroke="#9aa1ad" stroke-width="1.2"/></svg>
  </div>
  <div class="abs" style="left:679px;top:24px;font-size:13px;font-weight:500;color:var(--ink)">1800. 555. 014</div>
  <div class="abs" style="left:679px;top:44px;font-size:10px;color:var(--muted)">hello@tidewayco.com</div>
  <div class="btn" style="left:855px;top:27px;width:109px;height:31px;border-radius:16px;font-weight:600">LET'S TALK</div>
</header>

<nav class="nav abs">
  <a>Home</a><a>About me</a><a>Blog</a><a>Contact us</a>
  <div class="search">Search here
    <svg class="abs" style="right:14px;top:17px" width="14" height="14" viewBox="0 0 14 14"><circle cx="6" cy="6" r="4.5" fill="none" stroke="#fff" stroke-width="1.3"/><path d="M9.5 9.5l3 3" stroke="#fff" stroke-width="1.3"/></svg>
  </div>
</nav>

<section class="section" style="top:115px;height:463px">
  <div class="photo" role="img" aria-label="Bright workshop space with a facilitator standing by the window" style="left:0;top:0;width:1200px;height:463px;background:linear-gradient(100deg,#f4f5f7 0%,#eceef1 45%,#d3d8de 70%,#e9ebee 100%)"></div>
  <h1 class="hero-title abs" style="left:232px;top:127px">Learning that <b>grows</b><br><b>your tribe!</b></h1>
  <p class="abs" style="left:234px;top:246px;font-size:12px;color:var(--ink)">Experiential learning journeys that build culture and a growth mindset</p>
  <div class="btn" style="left:234px;top:299px;width:119px;height:31px;border:1px solid var(--navy);border-radius:0;font-weight:400">More About me</div>
</section>

<section class="section" style="top:578px;height:501px">
  <h2 class="heading abs" style="left:230px;top:108px">We’re <b>shaping courageous culture</b></h2>
  <p class="abs" style="left:234px;top:173px;font-size:11.5px;color:var(--ink)">Bespoke learning for small to medium teams across Australasia</p>

  <svg class="abs" style="left:234px;top:266px" width="32" height="28" viewBox="0 0 32 28"><rect x="1" y="1" width="30" height="20" fill="none" stroke="#24427f" stroke-width="1.4"/><path d="M5 16l7-7 5 5 9-9M16 21v5M11 27h10" fill="none" stroke="#24427f" stroke-width="1.4"/></svg>
  <svg class="abs" style="left:490px;top:262px" width="32" height="32" viewBox="0 0 32 32"><rect x="4" y="2" width="20" height="26" fill="none" stroke="#24427f" stroke-width="1.4"/><path d="M8 8h12M8 13h12M8 18h8" stroke="#24427f" stroke-width="1.4"/><circle cx="25" cy="24" r="5" fill="#fff" stroke="#24427f" stroke-width="1.4"/></svg>
  <svg class="abs" style="left:753px;top:266px" width="32" height="28" viewBox="0 0 32 28"><rect x="1" y="7" width="30" height="20" rx="2" fill="none" stroke="#24427f" stroke-width="1.4"/><path d="M11 7V2h10v5M1 15h30" fill="none" stroke="#24427f" stroke-width="1.4"/></svg>

  <div class="feat abs" style="left:234px;top:314px"><h3>Culture Insight</h3><p class="small">A holistic look at your organisation to find what your people need to thrive and grow together.</p></div>
  <div class="feat abs" style="left:490px;top:314px"><h3>Experiential Design</h3><p class="small">Hands-on learning built around your team, so new skills stick long after the workshop ends.</p></div>
  <div class="feat abs" style="left:753px;top:314px"><h3>Coaching &amp; Facilitation</h3><p class="small">Courageous, engaging sessions that challenge thinking and nurture a growth mindset.</p></div>
</section>

<section class="section" style="top:1079px;height:501px;background:var(--soft)">
  <h2 class="heading abs" style="left:234px;top:89px">Learning <b>journeys I design</b></h2>
  <svg width="0" height="0" style="position:absolute"><defs><polygon id="hx" points="27,1 52,15 52,43 27,57 2,43 2,15" fill="#24427f"/></defs></svg>

  <svg class="hex" style="left:232px;top:193px" viewBox="0 0 54 58"><use href="#hx"/><path d="M19 23l8-4 8 4v10l-8 4-8-4z" fill="none" stroke="#fff" stroke-width="1.5"/></svg>
  <svg class="hex" style="left:486px;top:193px" viewBox="0 0 54 58"><use href="#hx"/><circle cx="27" cy="29" r="9" fill="none" stroke="#fff" stroke-width="1.5"/><path d="M27 24v5l3 3" stroke="#fff" stroke-width="1.5" fill="none"/></svg>
  <svg class="hex" style="left:740px;top:193px" viewBox="0 0 54 58"><use href="#hx"/><path d="M18 37h18M20 35v-6M26 35v-10M32 35v-13" stroke="#fff" stroke-width="2"/></svg>
  <svg class="hex" style="left:232px;top:328px" viewBox="0 0 54 58"><use href="#hx"/><circle cx="27" cy="25" r="5" fill="none" stroke="#fff" stroke-width="1.5"/><path d="M18 38q9-12 18 0" fill="none" stroke="#fff" stroke-width="1.5"/></svg>
  <svg class="hex" style="left:486px;top:328px" viewBox="0 0 54 58"><use href="#hx"/><rect x="17" y="23" width="20" height="14" fill="none" stroke="#fff" stroke-width="1.5"/><path d="M23 23v-3h8v3M17 29h20" stroke="#fff" stroke-width="1.5" fill="none"/></svg>
  <svg class="hex" style="left:740px;top:328px" viewBox="0 0 54 58"><use href="#hx"/><rect x="19" y="20" width="16" height="18" fill="none" stroke="#fff" stroke-width="1.5"/><path d="M22 26h10M22 30h10M22 34h6" stroke="#fff" stroke-width="1.5"/></svg>

  <div class="svc abs" style="left:306px;top:192px"><h3>Team Workshops</h3><p>Engaging, hands-on sessions that bring people together to learn by doing.</p></div>
  <div class="svc abs" style="left:561px;top:192px"><h3>Change Programs</h3><p>Fluid, adaptable support that helps teams move through change with courage.</p></div>
  <div class="svc abs" style="left:815px;top:192px"><h3>Growth Mindset</h3><p>Practical tools that weave curiosity and resilience into everyday work.</p></div>
  <div class="svc abs" style="left:306px;top:324px"><h3>Leadership Journeys</h3><p>Bespoke pathways that grow confident leaders who nurture their tribe.</p></div>
  <div class="svc abs" style="left:561px;top:324px"><h3>Team Retreats</h3><p>Immersive off-site experiences that reset culture and build real trust.</p></div>
  <div class="svc abs" style="left:815px;top:324px"><h3>Culture Review</h3><p>A clear picture of where your culture is now and where it can grow next.</p></div>
</section>

<section class="section" style="top:1580px;height:572px">
  <div class="photo" role="img" aria-label="Smiling facilitator in a blue sweater" style="left:248px;top:88px;width:275px;height:484px;background:linear-gradient(180deg,#f1f3f6 0%,#aebfd8 45%,#7f97bd 100%);border-radius:120px 120px 0 0"></div>
  <h2 class="heading abs" style="left:645px;top:95px;font-size:31px;line-height:41px">I’m a Creative <b>Change</b><br><b>&amp; Culture Builder</b></h2>
  <div class="abs" style="left:647px;top:213px;font-size:11px;display:flex;gap:22px">
    <span style="color:var(--navy);font-weight:500;border-bottom:1px solid var(--navy)">My Story</span><span style="color:var(--muted)">Approach</span><span style="color:var(--muted)">Skills</span>
  </div>
  <p class="abs small" style="left:646px;top:256px;width:320px;font-size:9.5px">A Kiwi learning designer who helps businesses grow and nurture their tribes. I look at the whole organisation, find what is needed, and design experiential learning that builds a positive culture with growth woven in.</p>
  <div class="photo" role="img" aria-label="Portrait of the founder" style="left:646px;top:365px;width:44px;height:44px;border-radius:50%;background:#d8c3b2"></div>
  <div class="abs" style="left:715px;top:366px;font-size:12px;font-weight:500;color:var(--ink)">Aroha Tane</div>
  <div class="abs" style="left:715px;top:387px;font-size:9px;color:var(--muted)">Founder &amp; Learning Designer</div>
  <div class="btn" style="left:646px;top:443px;width:107px;height:31px">Learn More</div>
</section>

<section class="section" style="top:2152px;height:224px;background:var(--navy)">
  <div class="abs" style="right:747px;top:60px;text-align:right;color:#fff;font-size:23px;line-height:35px;font-weight:300;white-space:nowrap">We Have<br><b style="font-weight:600">Grown Many<br>Tribes So Far!!</b></div>
  <div class="stat abs" style="left:527px;top:60px"><b>1,780+</b><span>Learners Engaged</span></div>
  <div class="stat abs" style="left:685px;top:60px"><b>85</b><span>Teams Nurtured</span></div>
  <div class="stat abs" style="left:829px;top:60px"><b>3,260+</b><span>Workshop Hours</span></div>
  <div class="abs" style="left:527px;top:150px;font-size:10px;color:#8da0c6">Need a bespoke learning journey? <span style="color:#fff">Call Us Now</span> Or <span style="color:#fff">Send Message</span></div>
</section>

<section class="section" style="top:2376px;height:560px">
  <h2 class="heading abs" style="left:230px;top:96px">Our <b>Creative Tribe</b></h2>
  <p class="abs" style="left:234px;top:149px;font-size:11.5px;color:var(--ink)">Facilitators and coaches ready to take your team on the journey!!</p>
  <div class="abs" style="left:919px;top:141px;width:21px;height:21px;border:1px solid var(--line);color:var(--muted);font-size:12px;text-align:center;line-height:19px">‹</div>
  <div class="abs" style="left:943px;top:141px;width:21px;height:21px;border:1px solid var(--navy);color:var(--navy);font-size:12px;text-align:center;line-height:19px">›</div>

  <div class="member abs" style="left:234px;top:215px"><div class="ph" role="img" aria-label="Team member portrait" style="background:linear-gradient(180deg,#e9e6e1,#6c6a6c)"></div><h4>Aroha Tane</h4><span>Lead Learning Designer</span></div>
  <div class="member abs" style="left:421px;top:215px"><div class="ph" role="img" aria-label="Team member portrait" style="background:linear-gradient(180deg,#eeeae6,#b9b2aa)"></div><h4>Mere Walsh</h4><span>Culture Researcher</span></div>
  <div class="member abs" style="left:609px;top:215px"><div class="ph" role="img" aria-label="Team member portrait" style="background:linear-gradient(180deg,#e7ebe8,#8f8a6c)"></div><h4>Leon Hartley</h4><span>Workshop Facilitator</span></div>
  <div class="member abs" style="left:796px;top:215px"><div class="ph" role="img" aria-label="Team member portrait" style="background:linear-gradient(180deg,#eef0f3,#b9c6d6)"></div><h4>Tomas Reid</h4><span>Leadership Coach</span></div>
</section>

<section class="section" style="top:2936px;height:490px;border-top:1px solid #f0f1f4">
  <h2 class="heading abs" style="left:0;width:1200px;text-align:center;top:86px">What <b>Teams Say</b></h2>
  <div class="quote abs" style="left:234px;top:180px;width:347px;height:117px">The retreat changed how our team talks to each other. Hands-on, fun and challenging, and we still use the tools every week.</div>
  <div class="quote abs" style="left:618px;top:180px;width:348px;height:117px">A bespoke program that fit our people perfectly. Our leaders came back braver, more curious and ready to grow.</div>
  <div class="photo" role="img" aria-label="Client portrait" style="left:255px;top:324px;width:38px;height:38px;border-radius:50%;background:#e5d4c8"></div>
  <div class="abs" style="left:318px;top:328px;font-size:10px;font-weight:600;color:var(--ink)">KIRI DOYLE</div>
  <div class="abs" style="left:318px;top:346px;font-size:9px;color:var(--muted)">People &amp; Culture Lead</div>
  <div class="photo" role="img" aria-label="Client portrait" style="left:638px;top:324px;width:38px;height:38px;border-radius:50%;background:#d9d1c9"></div>
  <div class="abs" style="left:702px;top:328px;font-size:10px;font-weight:600;color:var(--ink)">SAM PARATA</div>
  <div class="abs" style="left:702px;top:346px;font-size:9px;color:var(--muted)">Operations Manager</div>
  <div class="abs" style="left:584px;top:421px;display:flex;gap:5px">
    <i style="width:7px;height:7px;border-radius:50%;background:var(--navy)"></i><i style="width:7px;height:7px;border-radius:50%;border:1px solid #c5ccd8"></i><i style="width:7px;height:7px;border-radius:50%;border:1px solid #c5ccd8"></i>
  </div>
</section>

<section class="section" style="top:3426px;height:449px">
  <div class="photo" role="img" aria-label="Two colleagues exploring ideas on a tablet during a workshop" style="left:0;top:0;width:552px;height:449px;background:linear-gradient(120deg,#dfe6ef 0%,#c7d3e2 50%,#9eb0c7 100%)"></div>
  <div class="abs" style="left:552px;top:0;width:648px;height:449px;background:var(--navy)"></div>
  <div class="abs" style="left:618px;top:68px;font-size:10px;color:#7f93bd">Start the Journey</div>
  <div class="abs" style="left:618px;top:90px;font-size:22px;color:#fff;font-weight:500">Free Discovery Chat</div>
  <div class="field" style="left:620px;top:156px;width:156px;height:31px">Your Name</div>
  <div class="field" style="left:792px;top:156px;width:172px;height:31px">Your Email</div>
  <div class="field" style="left:620px;top:203px;width:344px;height:31px">Team Size</div>
  <div class="field" style="left:620px;top:250px;width:344px;height:80px">What would you like your team to learn?</div>
  <div class="abs" style="left:620px;top:343px;width:344px;height:32px;background:#3a5ba3;color:#fff;font-size:9px;font-weight:600;display:flex;align-items:center;justify-content:center">SEND REQUEST</div>
</section>

<section class="section" style="top:3875px;height:765px">
  <h2 class="heading abs" style="left:0;width:1200px;text-align:center;top:95px">Stories <b>from the journey</b></h2>
  <p class="abs" style="left:0;width:1200px;text-align:center;top:150px;font-size:11.5px;color:var(--ink)">Ideas, articles and lessons on learning, culture and growth from the blog.</p>

  <div class="card" style="left:234px;top:210px;width:230px;height:305px"><div class="ph" role="img" aria-label="Team collaborating around a table" style="background:linear-gradient(135deg,#c9d2dc,#6d7480)"></div><div class="body"><em>Culture, Teams</em><h4>Growing a growth mindset.</h4><p>Small daily habits that help teams stay curious and adaptable.</p><a>Read More →</a></div></div>
  <div class="card" style="left:486px;top:210px;width:230px;height:305px"><div class="ph" role="img" aria-label="Leader reflecting at a desk" style="background:linear-gradient(135deg,#f1e7e2,#b5a59d)"></div><div class="body"><em>Leadership</em><h4>Leading with courage.</h4><p>Why brave conversations build stronger and kinder tribes.</p><a>Read More →</a></div></div>
  <div class="card" style="left:736px;top:210px;width:230px;height:305px"><div class="ph" role="img" aria-label="Person planning a workshop on a laptop" style="background:linear-gradient(135deg,#eef1f4,#b6bfca)"></div><div class="body"><em>Learning Design</em><h4>Learning by doing.</h4><p>How experiential sessions turn new skills into lasting change.</p><a>Read More →</a></div></div>

  <div class="abs" style="left:232px;top:597px;width:160px;text-align:right;color:var(--navy);font-size:28px;line-height:39px;font-weight:300">Who<br><b style="font-weight:600">Trusts us</b></div>
  <div class="partner" style="left:421px;top:601px;width:170px"><i></i></div>
  <div class="partner" style="left:617px;top:601px;width:169px"><i></i></div>
  <div class="partner" style="left:798px;top:601px;width:168px"><i></i></div>
</section>

<footer class="section footer">
  <div class="abs" style="left:234px;top:34px;font-size:17px;color:#fff">Ready to grow your tribe <b style="font-weight:600">or build a stronger culture?</b></div>
  <div class="abs" style="left:827px;top:27px;width:137px;height:33px;background:var(--navy);color:#fff;font-size:9px;font-weight:600;display:flex;align-items:center;justify-content:center">CONTACT US NOW!!</div>
  <div class="abs" style="left:234px;top:88px;width:730px;height:1px;background:#2a2e38"></div>

  <div class="abs" style="left:234px;top:125px;display:flex;align-items:center;gap:10px">
    <i style="width:30px;height:30px;border-radius:50%;background:var(--navy);display:block"></i>
    <div><div style="font-size:19px;color:#fff;line-height:22px">Tideway</div><div style="font-size:9px;color:#7d8391">Learning &amp; Development Studio</div></div>
  </div>
  <p class="abs" style="left:234px;top:178px;width:205px;font-size:9.5px;line-height:18px">Tideway designs experiential learning that helps businesses grow and nurture their tribes.</p>
  <div class="abs" style="left:234px;top:251px;width:203px;height:31px;background:#fff;font-size:9px;color:var(--muted);padding:9px 12px">Enter your email</div>

  <div class="abs" style="left:486px;top:116px"><h5>Quick Links</h5><ul><li>Home</li><li>About me</li><li>Blog</li><li>Contact Us</li><li>Find us</li></ul></div>

  <div class="abs" style="left:630px;top:116px;width:150px"><h5>Latest Articles</h5>
    <p style="font-size:10px;line-height:16px;color:#d5d8de">Five ways to grow a learning culture.</p>
    <p style="font-size:9px;color:#5a76b8;margin:2px 0 12px">13 Feb, 2021 / Culture</p>
    <p style="font-size:10px;line-height:16px;color:#d5d8de">What makes a workshop really stick.</p>
    <p style="font-size:9px;color:#5a76b8">02 Mar, 2021 / Learning</p>
  </div>

  <div class="abs" style="left:806px;top:116px;width:170px"><h5>Find Us</h5>
    <div style="display:flex;gap:12px;font-size:9.5px;line-height:16px">
      <svg width="14" height="18" viewBox="0 0 14 18"><path d="M7 17s6-6 6-10A6 6 0 0 0 1 7c0 4 6 10 6 10z" fill="none" stroke="#fff" stroke-width="1.3"/><circle cx="7" cy="7" r="2" fill="#fff"/></svg>
      <span>14 Harbour Lane, Kelburn Road 6012, NZ</span></div>
    <div style="display:flex;gap:12px;font-size:9.5px;margin-top:14px;align-items:center">
      <svg width="14" height="14" viewBox="0 0 14 14"><path d="M2 1h3l1 3-2 1.5q1.5 3 3.5 3.5L9 7l3 1v3q-10 1-10-10z" fill="none" stroke="#fff" stroke-width="1.2"/></svg>+64 21 555 0184</div>
    <div style="display:flex;gap:12px;font-size:9.5px;margin-top:14px;align-items:center">
      <svg width="14" height="11" viewBox="0 0 14 11"><rect x="1" y="1" width="12" height="9" fill="none" stroke="#fff" stroke-width="1.2"/><path d="M1 1l6 5 6-5" fill="none" stroke="#fff" stroke-width="1.2"/></svg>studio@tidewayco.com</div>
    <div class="social" style="margin-top:16px"><i style="border-color:#fff"></i><i></i><i></i><i></i></div>
  </div>

  <div class="abs" style="left:0;top:330px;width:1200px;height:1px;background:#23272f"></div>
  <div class="abs" style="left:234px;top:349px;font-size:10px;color:#fff">Copyright <span style="color:#5a76b8">Tideway</span> @ 2021</div>
  <div class="abs" style="left:806px;top:349px;font-size:10px;display:flex;gap:22px"><span style="color:#fff">Privacy</span><span>Terms</span><span>Accounts</span></div>
</footer>

</body>
</html>
```